Need Primer (paint) Label Design

THE ATTACHED LABEL/S ARE SOLEY FOR REFERENCE. DO NOT MAKE ME AN INTERIOR PAINT OR CHALK PAINT LABEL. I ONLY NEED A "PRIMER" LABEL. THE ATTACHED INTERIOR PAINT LABEL IS ONLY TO SHOW YOU THE THEME/DESIGN OF OUR OTHER LABELS. THE BLUE LABEL ONLY HAS A DESIGN ASPECT I LIKE (PRIMER ON SIDE). The last four labels are our competitors.
```````````````````````````````````````````````````````````````````````````````````````````````````
We need this label to look professional, sharp, eye catching and modern.
OUR PRIMARY COLORS ARE BLACK AND WHITE. IF YOU INCOPORATE ANOTHER COLOR, SILVER OR GOLD MIGHT BE IDEAL BUT PLEASE DON'T DRIFT TOO FAR.
The attached documents:
1st - Our Logo
2nd - Our chalk paint label (reference). We do not need a chalk paint label.
3rd. A random design example. I like the PRIME on the side running vertically. I think it's a cool design concept.
````````````````````````````````````````````````````````````````````````````````````````````````````
We are going to be using a normal paint can with a metal bail/handle so please use that with you design work
``````````````````````````````````````````````````````````````````````````````````````````````````
Order, in my head:
4327
Coatings
^^ I want this to stand out as well but I don't want it to be the first thing your eye is drawn to. Probably 2nd
Interior/Exterior
Multi - Surface Primer
^^ Want this to stick out and draw your eye so the customer knows what it is immediately
Exceptional Adhesion, Performance, Durability,
Use on Wood, Drywall, Plaster, Stucco, Masonry, Brick, Paneling, Painted Metal, & Properly Prepared Glossy Surfaces & More
35* Lowe Temperature Application (can be on side or small)
100% Acrylic
Low Odor - Low VOC - Soap & Water Clean Up
1 US Gallon - 3.785 L
Feel free to get creative with it!

```html
<!DOCTYPE html>
<html lang="en">
<head>
<meta charset="utf-8">
<title>4327 Coatings — Multi-Surface Primer Label</title>
<link href="https://fonts.googleapis.com/css2?family=Bebas+Neue&family=Montserrat:wght@500;600;800&display=swap" rel="stylesheet">
<style>
  :root {
    --backdrop: #3d3d3d;
    --label-black: #000000;
    --ink-white: #ffffff;
    --silver-light: #e6e6e6;
    --silver-mid: #a9a9a9;
    --silver-dark: #5c5c5c;
    --band-text: #1a1a1a;
  }
  html, body {
    margin: 0;
    padding: 0;
    width: 1200px;
    height: 792px;
    overflow: hidden;
    background: var(--backdrop);
  }
  .canvas {
    position: relative;
    width: 1200px;
    height: 792px;
  }
  .primer-label {
    position: absolute;
    left: 220px;
    top: 28px;
    width: 760px;
    height: 736px;
    background: var(--label-black);
  }
  .primer-label svg {
    display: block;
  }
  .product-word {
    font-family: "Montserrat", sans-serif;
    font-weight: 800;
    fill: var(--ink-white);
  }
  .brand-name {
    font-family: "Bebas Neue", sans-serif;
    fill: var(--ink-white);
  }
  .use-heading {
    font-family: "Bebas Neue", sans-serif;
    fill: var(--ink-white);
  }
  .band-text {
    font-family: "Bebas Neue", sans-serif;
    fill: var(--band-text);
  }
  .benefit-pill {
    fill: var(--ink-white);
  }
  .benefit-text {
    font-family: "Montserrat", sans-serif;
    font-weight: 600;
    fill: var(--label-black);
  }
  .body-copy {
    font-family: "Montserrat", sans-serif;
    font-weight: 500;
    fill: var(--ink-white);
  }
  .volume {
    font-family: "Bebas Neue", sans-serif;
    fill: var(--ink-white);
  }
  .feature-ring {
    fill: none;
    stroke: var(--ink-white);
    stroke-width: 1.4;
  }
  .feature-icon {
    fill: var(--ink-white);
  }
  .feature-icon-line {
    fill: none;
    stroke: var(--ink-white);
    stroke-width: 1;
    stroke-linecap: round;
  }
  .feature-text {
    font-family: "Montserrat", sans-serif;
    font-weight: 800;
    fill: var(--ink-white);
  }
  .feature-subtext {
    font-family: "Montserrat", sans-serif;
    font-weight: 500;
    fill: var(--ink-white);
  }
  .divider {
    stroke: var(--ink-white);
    stroke-width: 0.8;
  }
</style>
</head>
<body>
<main class="canvas">
  <section class="primer-label" aria-label="4327 Coatings interior/exterior multi-surface primer label">
    <svg width="760" height="736" viewBox="0 0 760 736" xmlns="http://www.w3.org/2000/svg">
      <defs>
        <linearGradient id="silver-band" x1="0" y1="0" x2="1" y2="0">
          <stop offset="0" stop-color="var(--silver-dark)"/>
          <stop offset="0.25" stop-color="var(--silver-light)"/>
          <stop offset="0.55" stop-color="var(--silver-mid)"/>
          <stop offset="0.8" stop-color="var(--silver-light)"/>
          <stop offset="1" stop-color="var(--silver-mid)"/>
        </linearGradient>
      </defs>

      <!-- Vertical product word -->
      <text class="product-word" transform="translate(249 643) rotate(-90)" x="0" y="0"
            font-size="214" textLength="551" lengthAdjust="spacingAndGlyphs">PRIMER</text>

      <!-- Brand name, single line -->
      <text class="brand-name" x="301" y="418" font-size="62" textLength="283" lengthAdjust="spacingAndGlyphs">4327 COATINGS</text>

      <!-- Use heading -->
      <text class="use-heading" x="301" y="467" font-size="42" textLength="283" lengthAdjust="spacingAndGlyphs">INTERIOR/EXTERIOR</text>

      <!-- Silver product band -->
      <polygon points="296,473 625,473 610,508 281,508" fill="url(#silver-band)"/>
      <text class="band-text" x="302" y="499" font-size="25" textLength="302" lengthAdjust="spacing">MULTI - SURFACE PRIMER</text>

      <!-- Benefit pills -->
      <polygon class="benefit-pill" points="298,515 402,515 407,529 303,529"/>
      <text class="benefit-text" x="306" y="525" font-size="6.6">EXCEPTIONAL ADHESION</text>
      <polygon class="benefit-pill" points="407,515 469,515 474,529 412,529"/>
      <text class="benefit-text" x="417" y="525" font-size="6.6">PERFORMANCE</text>
      <polygon class="benefit-pill" points="474,515 525,515 530,529 479,529"/>
      <text class="benefit-text" x="484" y="525" font-size="6.6">DURABILITY</text>

      <!-- Surfaces -->
      <text class="body-copy" x="301" y="560" font-size="9.2">Use on Wood, Drywall, Plaster, Stucco, Masonry, Brick, Paneling,</text>
      <text class="body-copy" x="301" y="572" font-size="9.2">Painted Metal, &amp; Properly Prepared Glossy Surfaces &amp; More</text>
      <line class="divider" x1="301" y1="581" x2="393" y2="581"/>
      <text class="body-copy" x="301" y="598" font-size="7.6">35º Lower Temperature Application</text>

      <!-- Volume -->
      <text class="volume" x="301" y="643" font-size="28" textLength="174" lengthAdjust="spacingAndGlyphs">1 US GALLON - 3.785 L</text>

      <!-- Feature badges -->
      <g class="feature-badge" transform="translate(678 459)">
        <circle class="feature-ring" r="20"/>
        <path class="feature-icon" d="M-4,-14 h8 l-1,9 h-6 z"/>
        <text class="feature-text" x="0" y="2" font-size="8" text-anchor="middle">100%</text>
        <text class="feature-subtext" x="0" y="9" font-size="5" text-anchor="middle">ACRYLIC</text>
      </g>
      <g class="feature-badge" transform="translate(678 512)">
        <circle class="feature-ring" r="20"/>
        <path class="feature-icon" d="M0,-15 l4,9 h-8 z"/>
        <path class="feature-icon-line" d="M-3,-4 v3 M0,-4 v3 M3,-4 v3"/>
        <text class="feature-text" x="0" y="6" font-size="7.5" text-anchor="middle">LOW</text>
        <text class="feature-subtext" x="0" y="12" font-size="5" text-anchor="middle">ODOR</text>
      </g>
      <g class="feature-badge" transform="translate(678 565)">
        <circle class="feature-ring" r="20"/>
        <path class="feature-icon-line" d="M-3,-15 q2,2 0,4 M0,-15 q2,2 0,4 M3,-15 q2,2 0,4"/>
        <circle class="feature-icon" cx="0" cy="-5" r="3"/>
        <text class="feature-text" x="0" y="6" font-size="7.5" text-anchor="middle">LOW</text>
        <text class="feature-subtext" x="0" y="12" font-size="5" text-anchor="middle">VOC</text>
      </g>
      <g class="feature-badge" transform="translate(678 620)">
        <circle class="feature-ring" r="20"/>
        <path class="feature-icon" d="M-5,-12 h10 l-2,10 h-6 z"/>
        <text class="feature-text" x="0" y="5" font-size="4.2" text-anchor="middle">SOAP &amp; WATER</text>
        <text class="feature-subtext" x="0" y="10" font-size="3.6" text-anchor="middle">CLEAN UP</text>
      </g>
    </svg>
  </section>
</main>
</body>
</html>
```